Nectarine Point of Sale Cards for Grocery Retail Markets

We are looking to update our Nectarine point of sale card and price card. The cards will need to be 7" x 11" with a .125 bleed - one sided. See attached for the old versions. We would like this to use photos that look like true Washington State Peaches. Here are the bullet points we would like to use: - New Crop!- Tree Ripened- Excellent FlavorNOTE: The price card just needs to have a space where a retailer can write in the sale price of the item. See attachment with the white box.

Target Market(s)

Retail market shoppers

Requirements
Must have
• Pictures of Nectarines Only

```html
<!DOCTYPE html>
<html lang="en">
<head>
<meta charset="utf-8">
<title>Nectarine Point of Sale Cards</title>
<link rel="stylesheet" href="https://fonts.googleapis.com/css2?family=Oswald:wght@600;700&family=Great+Vibes&family=Raleway:wght@500&display=swap">
<style>
  :root {
    --page-bg: #eeedf0;
    --band-white: #ffffff;
    --title-red: #c8202e;
    --brand-green: #1f7a35;
    --brand-dot: #e0573a;
    --bullet-cream: #f6f2a4;
    --script-white: #ffffff;
    --label-ink: #222222;
    --divider: #cccccc;
    --fruit-deep: #5a1418;
    --fruit-mid: #a3343a;
    --fruit-light: #cf6a5c;
    --fruit-glow: #d99a5a;
  }
  * { margin: 0; padding: 0; box-sizing: border-box; }
  html, body { width: 908px; height: 1200px; overflow: hidden; }
  body { background: var(--page-bg); position: relative; font-family: "Oswald", sans-serif; }

  .pos-card {
    position: absolute;
    left: 78px;
    width: 753px;
    height: 477px;
    overflow: hidden;
    box-shadow: 0 14px 18px -8px rgba(0,0,0,0.35);
  }
  .pos-card--front { top: 61px; }
  .pos-card--back { top: 627px; }

  .fruit-photo {
    position: absolute; inset: 0;
    background:
      radial-gradient(ellipse 30% 35% at 25% 45%, var(--fruit-glow) 0%, transparent 70%),
      radial-gradient(ellipse 35% 40% at 80% 45%, var(--fruit-light) 0%, transparent 75%),
      radial-gradient(ellipse 30% 35% at 62% 80%, var(--fruit-light) 0%, transparent 75%),
      linear-gradient(135deg, var(--fruit-mid) 0%, var(--fruit-deep) 55%, var(--fruit-mid) 100%);
  }

  .header-band {
    position: absolute; left: 0; right: 0; top: 12px; height: 66px;
    background: var(--band-white);
  }
  .product-title {
    position: absolute; left: 27px; top: 6px;
    font-weight: 700; font-size: 40px; line-height: 54px;
    color: var(--title-red); letter-spacing: 0.3px;
  }
  .header-divider {
    position: absolute; left: 518px; top: 14px; width: 1px; height: 38px;
    background: var(--divider);
  }
  .brand-dot {
    position: absolute; left: 536px; top: 9px; width: 50px; height: 50px;
    border-radius: 50%; background: var(--brand-dot);
  }
  .brand-name {
    position: absolute; left: 598px; top: 16px;
    font-family: "Raleway", sans-serif; font-weight: 500;
    font-size: 14px; line-height: 16px; color: var(--brand-green);
  }

  .tagline {
    position: absolute; left: 28px; top: 84px;
    font-family: "Great Vibes", cursive;
    font-size: 72px; line-height: 80px;
    color: var(--script-white);
  }

  .selling-points {
    position: absolute; left: 30px; top: 306px; list-style: none;
  }
  .selling-points li {
    display: flex; align-items: center; height: 54.5px;
    font-weight: 700; font-size: 36px; color: var(--bullet-cream);
    text-shadow: 0 1px 3px rgba(0,0,0,0.35);
  }
  .bullet-icon { width: 26px; height: 26px; margin-right: 14px; flex: none; }

  .price-box {
    position: absolute; left: 550px; top: 277px; width: 203px; height: 200px;
    background: var(--band-white);
  }
  .price-box::after {
    content: ""; position: absolute; inset: 5px 4px 5px 6px;
    border: 1.5px dashed #444;
  }

  .side-label {
    position: absolute; left: 0; width: 908px; text-align: center;
    font-family: "Raleway", sans-serif; font-weight: 500;
    font-size: 34px; color: var(--label-ink);
  }
  .side-label--front { top: 552px; }
  .side-label--back { top: 1124px; }
</style>
</head>
<body>

<section class="pos-card pos-card--front">
  <div class="fruit-photo" role="img" aria-label="Close-up photo of ripe red nectarines with a green leaf"></div>
  <header class="header-band">
    <h1 class="product-title">WASHING STATE NECTARINES</h1>
    <span class="header-divider"></span>
    <span class="brand-dot"></span>
    <p class="brand-name">Evergreen Orchard<br>Growers</p>
  </header>
  <p class="tagline">Taste the Difference!</p>
  <ul class="selling-points">
    <li><svg class="bullet-icon" viewBox="0 0 26 26"><circle cx="13" cy="13" r="12" fill="var(--bullet-cream)"/><circle cx="13" cy="14" r="6" fill="var(--fruit-deep)"/></svg>NEW CROP!</li>
    <li><svg class="bullet-icon" viewBox="0 0 26 26"><circle cx="13" cy="13" r="12" fill="var(--bullet-cream)"/><circle cx="13" cy="10" r="5" fill="var(--fruit-deep)"/><rect x="12" y="13" width="2" height="7" fill="var(--fruit-deep)"/></svg>TREE RIPENED</li>
    <li><svg class="bullet-icon" viewBox="0 0 26 26"><circle cx="13" cy="13" r="12" fill="var(--bullet-cream)"/><rect x="9" y="7" width="8" height="12" rx="2" fill="var(--fruit-deep)"/></svg>EXCELLENT FLAVOR</li>
  </ul>
</section>
<p class="side-label side-label--front">Front</p>

<section class="pos-card pos-card--back">
  <div class="fruit-photo" role="img" aria-label="Close-up photo of ripe red nectarines with a green leaf"></div>
  <header class="header-band">
    <h2 class="product-title">WASHING STATE NECTARINES</h2>
    <span class="header-divider"></span>
    <span class="brand-dot"></span>
    <p class="brand-name">Evergreen Orchard<br>Growers</p>
  </header>
  <p class="tagline">Taste the Difference!</p>
  <ul class="selling-points">
    <li><svg class="bullet-icon" viewBox="0 0 26 26"><circle cx="13" cy="13" r="12" fill="var(--bullet-cream)"/><circle cx="13" cy="14" r="6" fill="var(--fruit-deep)"/></svg>NEW CROP!</li>
    <li><svg class="bullet-icon" viewBox="0 0 26 26"><circle cx="13" cy="13" r="12" fill="var(--bullet-cream)"/><circle cx="13" cy="10" r="5" fill="var(--fruit-deep)"/><rect x="12" y="13" width="2" height="7" fill="var(--fruit-deep)"/></svg>TREE RIPENED</li>
    <li><svg class="bullet-icon" viewBox="0 0 26 26"><circle cx="13" cy="13" r="12" fill="var(--bullet-cream)"/><rect x="9" y="7" width="8" height="12" rx="2" fill="var(--fruit-deep)"/></svg>EXCELLENT FLAVOR</li>
  </ul>
  <div class="price-box" aria-label="Space for handwritten sale price"></div>
</section>
<p class="side-label side-label--back">Back</p>

</body>
</html>
```